Veltrix4 Business Card - Health

Veltrix4 maximizes value from the health data of its clients, including doctors, HMOs, and patients. I have attached the Veltrix4 logo as an ai and eps file.
Target Market(s)
Health, HMO, Healthcare, Data, Big Data, Data Analytics
Industry/Entity Type
Business
Requirements
Must have
- At least one side should have some white on it so that we can write on it.

```html
<!DOCTYPE html>
<html lang="en">
<head>
<meta charset="UTF-8">
<title>Veltrix4 Business Card</title>
<link href="https://fonts.googleapis.com/css2?family=Open+Sans:wght@400;600&display=swap" rel="stylesheet">
<style>
  :root {
    --stage: #3a3330;
    --card-dark: #1c1c1e;
    --card-dark-edge: #262628;
    --brand-blue: #0a9ee0;
    --brand-blue-light: #1aa9e8;
    --accent-blue: #2b8fd6;
    --mark-blue: #3b82e0;
    --text-white: #ffffff;
    --text-soft: #e6e6e6;
    --divider: #3c4550;
    --note-white: #ffffff;
    --note-rule: #d5e7f3;
  }
  * { margin: 0; padding: 0; box-sizing: border-box; }
  html, body {
    width: 1200px; height: 844px; overflow: hidden;
    background: var(--stage);
    font-family: "Open Sans", Arial, sans-serif;
  }
  .canvas {
    position: relative; width: 1200px; height: 844px;
    display: flex; align-items: center; justify-content: center; gap: 40px;
  }
  .card {
    width: 520px; height: 297px; position: relative; overflow: hidden;
    border-radius: 2px;
    box-shadow: 0 10px 30px rgba(0,0,0,0.45);
  }
  .card--front { background: linear-gradient(160deg, var(--card-dark-edge), var(--card-dark)); }
  .card--back { background: linear-gradient(135deg, var(--brand-blue-light), var(--brand-blue)); }

  .brand {
    position: absolute; display: flex; align-items: center; gap: 14px;
    color: var(--text-white); font-weight: 400; line-height: 1;
  }
  .card--front .brand { left: 34px; bottom: 58px; font-size: 44px; }
  .brand__dot {
    width: 50px; height: 50px; border-radius: 50%; background: var(--mark-blue);
  }
  .card--back .brand { right: 34px; top: 78px; font-size: 50px; }

  .note-area {
    position: absolute; left: 0; right: 0; bottom: 0; height: 96px;
    background: var(--note-white);
    padding: 30px 34px 0;
  }
  .note-area__line {
    height: 1px; background: var(--note-rule); margin-bottom: 28px;
  }

  .divider {
    position: absolute; left: 302px; top: 40px; width: 1px; height: 190px;
    background: var(--divider);
  }
  .contact {
    position: absolute; left: 322px; top: 44px; color: var(--text-soft);
    font-size: 12.5px; line-height: 1.35;
  }
  .contact__name { color: var(--accent-blue); font-weight: 600; font-size: 15px; line-height: 1.2; }
  .contact__title { margin-bottom: 18px; }
  .contact__address { margin-bottom: 16px; }
  .contact__line { display: flex; align-items: center; gap: 8px; }
  .contact__icon { width: 11px; height: 11px; flex: none; fill: var(--accent-blue); }
</style>
</head>
<body>
<main class="canvas">
  <section class="card card--front" aria-label="Card front">
    <div class="brand">
      <span class="brand__dot"></span>
      <span class="brand__name">Veltrix4</span>
    </div>
    <div class="divider"></div>
    <div class="contact">
      <p class="contact__name">Marcus Ellwood</p>
      <p class="contact__title">Managing Director</p>
      <p class="contact__address">48 Harbor Lane, Suite 2<br>Northfield, 560021.</p>
      <p class="contact__line">
        <svg class="contact__icon" viewBox="0 0 24 24" aria-hidden="true"><path d="M6.6 10.8a15.1 15.1 0 0 0 6.6 6.6l2.2-2.2c.3-.3.7-.4 1-.2 1.1.4 2.3.6 3.6.6.6 0 1 .4 1 1V20c0 .6-.4 1-1 1C10.6 21 3 13.4 3 4c0-.6.4-1 1-1h3.5c.6 0 1 .4 1 1 0 1.3.2 2.5.6 3.6.1.3 0 .7-.2 1z"/></svg>
        044-987 654 321
      </p>
      <p class="contact__line">
        <svg class="contact__icon" viewBox="0 0 24 24" aria-hidden="true"><path d="M2 5h20v14H2z M2 5l10 8 10-8" stroke="#1c1c1e" stroke-width="1.5"/></svg>
        hello@veltrixmail.com
      </p>
      <p class="contact__line">
        <svg class="contact__icon" viewBox="0 0 24 24" aria-hidden="true"><path d="M10 14a5 5 0 0 1 0-7l3-3a5 5 0 0 1 7 7l-1.5 1.5-1.4-1.4L18.6 9.6a3 3 0 0 0-4.2-4.2l-3 3a3 3 0 0 0 0 4.2zM14 10a5 5 0 0 1 0 7l-3 3a5 5 0 0 1-7-7l1.5-1.5 1.4 1.4-1.5 1.5a3 3 0 0 0 4.2 4.2l3-3a3 3 0 0 0 0-4.2z"/></svg>
        www.veltrixhealth.com
      </p>
    </div>
  </section>

  <section class="card card--back" aria-label="Card back">
    <div class="brand">
      <span class="brand__name">Veltrix4</span>
    </div>
    <div class="note-area" aria-label="White writing area">
      <div class="note-area__line"></div>
      <div class="note-area__line"></div>
    </div>
  </section>
</main>
</body>
</html>
```